Orvan's Tableware

Need a package designed. Please go over the POWER POINT attached it has ALL of the details within. Package contains elegant high quality plastic dinner set.
Updates

Box size 32×27×16 cm

Target Market(s)

Wedding, party's

Requirements
Must have
• Power Point contains all of my must haves.
Nice to have
• Power Point contains all nice to haves.
Should not have
• Power Point contains all should not haves.

```html
<!DOCTYPE html>
<html lang="en">
<head>
<meta charset="utf-8">
<title>Orvan's Tableware – Gold Dinner Set Box</title>
<link rel="stylesheet" href="https://fonts.googleapis.com/css2?family=Montserrat:wght@500;600;700&family=Nunito:wght@800;900&family=Kanit:wght@700&display=swap">
<style>
  :root {
    --page-bg: #d6d6d6;
    --board: #eeeeec;
    --board-edge: #c9c9c6;
    --ink: #1c1c1c;
    --slate: #3d4a4a;
    --leaf-green: #6f9a3a;
    --leaf-dark: #3f7f2e;
    --leaf-light: #9cc7a6;
    --gold-light: #f2c868;
    --gold: #c98a1f;
    --gold-dark: #8a5510;
    --badge-green: #6b8e32;
    --muted: #8b8b86;
  }
  * { box-sizing: border-box; margin: 0; padding: 0; }
  html, body { width: 1200px; height: 873px; overflow: hidden; }
  body { background: var(--page-bg); font-family: "Montserrat", sans-serif; position: relative; }

  .panel {
    position: absolute;
    background: var(--board);
    border: 1px solid var(--board-edge);
    overflow: hidden;
  }
  .panel-top { left: 60px; top: 40px; width: 576px; height: 486px; }
  .panel-front { left: 60px; top: 526px; width: 576px; height: 288px; }
  .panel-side { left: 636px; top: 40px; width: 288px; height: 486px; }

  .bamboo {
    position: absolute;
    border-radius: 40% 60% 50% 45%;
    background: radial-gradient(ellipse at center, rgba(111,154,58,.75), rgba(156,199,166,.35) 60%, rgba(238,238,236,0) 75%);
  }

  .brand-name {
    font-family: "Montserrat", sans-serif;
    font-weight: 600;
    color: var(--ink);
    letter-spacing: .12em;
    text-transform: uppercase;
    white-space: nowrap;
    display: flex; align-items: center; gap: 10px;
  }
  .brand-mark { width: 14px; height: 14px; background: var(--ink); display: inline-block; }

  .top-title { position: absolute; left: 0; right: 0; top: 120px; text-align: center; display: flex; flex-direction: column; align-items: center; }
  .top-title .brand-name { font-size: 17px; margin-bottom: 10px; }
  .gold-word {
    font-family: "Kanit", sans-serif; font-weight: 700; font-size: 64px; line-height: 1;
    background: linear-gradient(180deg, var(--gold-light), var(--gold) 55%, var(--gold-dark));
    -webkit-background-clip: text; background-clip: text; color: transparent;
    letter-spacing: .03em;
  }
  .quality {
    font-family: "Nunito", sans-serif; font-weight: 900; font-size: 28px; color: var(--slate);
    letter-spacing: .04em; margin-top: 4px; padding: 0 10px 4px;
    border-bottom: 1.5px solid var(--slate);
  }
  .pieces { font-family: "Nunito", sans-serif; font-weight: 900; font-size: 26px; color: var(--leaf-green); margin-top: 4px; letter-spacing: .03em; }
  .bonus { font-size: 10px; font-weight: 500; color: var(--ink); margin-top: 2px; }
  .cutlery-badge { margin-top: 10px; width: 48px; height: 48px; }

  .sets-badge {
    position: absolute; right: 36px; top: 22px; width: 50px; height: 50px; border-radius: 50%;
    background: var(--badge-green); color: #fff; text-align: center;
    display: flex; flex-direction: column; justify-content: center; line-height: 1;
  }
  .sets-badge .num { font-family: "Nunito", sans-serif; font-weight: 900; font-size: 18px; }
  .sets-badge .word { font-size: 8px; font-weight: 600; letter-spacing: .1em; }

  .front-brand { position: absolute; left: 0; right: 0; top: 118px; display: flex; justify-content: center; }
  .front-brand .brand-name { font-size: 26px; }

  .side-list { position: absolute; left: 30px; right: 30px; top: 50px; display: flex; flex-direction: column; gap: 34px; }
  .side-item { display: flex; align-items: center; gap: 18px; }
  .plate { width: 100px; height: 100px; border-radius: 50%; flex: none; }
  .plate-gold { background: radial-gradient(circle, #ffffff 55%, #e9d9a8 60%, var(--gold) 72%, #e9d9a8 80%); }
  .plate-rose { background: radial-gradient(circle, #ffffff 55%, #ecd0c4 60%, #c98a72 72%, #ecd0c4 80%); }
  .forks { width: 100px; height: 100px; flex: none; background: linear-gradient(90deg, transparent 20%, var(--gold-light) 22%, var(--gold) 26%, transparent 28%, transparent 46%, var(--gold-light) 48%, var(--gold) 52%, transparent 54%, transparent 72%, var(--gold-light) 74%, var(--gold) 78%, transparent 80%); }
  .side-label { font-size: 13px; font-weight: 500; color: var(--muted); }
</style>
</head>
<body>

  <section class="panel panel-top" aria-label="Box lid">
    <div class="bamboo" role="img" aria-label="Watercolour bamboo stalks and leaves" style="left:20px;top:150px;width:240px;height:330px;"></div>
    <div class="bamboo" role="img" aria-label="Watercolour bamboo branch with leaves" style="left:330px;top:20px;width:240px;height:230px;"></div>

    <div class="sets-badge"><span class="num">25</span><span class="word">SETS</span></div>

    <div class="top-title">
      <div class="brand-name"><span class="brand-mark"></span>Orvan's Tableware</div>
      <div class="gold-word">GOLD</div>
      <div class="quality">QUALITY PLASTIC</div>
      <div class="pieces">150 PIECES</div>
      <div class="bonus">Bonus : Salad Plates / Desert Forks</div>
      <svg class="cutlery-badge" viewBox="0 0 48 48" aria-hidden="true">
        <defs>
          <radialGradient id="goldDisc" cx="40%" cy="35%" r="70%">
            <stop offset="0" stop-color="#f2c868"/>
            <stop offset=".6" stop-color="#c98a1f"/>
            <stop offset="1" stop-color="#8a5510"/>
          </radialGradient>
        </defs>
        <circle cx="24" cy="24" r="23" fill="url(#goldDisc)"/>
        <path d="M15 12v8a3 3 0 0 0 2 3v13h2V23a3 3 0 0 0 2-3v-8h-1v7h-1v-7h-1v7h-1v-7z" fill="#fff"/>
        <path d="M31 12c-3 2-4 6-4 11h3v13h2V12z" fill="#fff"/>
      </svg>
    </div>
  </section>

  <section class="panel panel-front" aria-label="Box front">
    <div class="bamboo" role="img" aria-label="Watercolour bamboo stalks and leaves" style="left:10px;top:70px;width:200px;height:230px;"></div>
    <div class="bamboo" role="img" aria-label="Watercolour bamboo stalks and leaves" style="left:400px;top:-10px;width:190px;height:220px;"></div>
    <div class="front-brand">
      <div class="brand-name"><span class="brand-mark" style="width:20px;height:20px;"></span>Orvan's Tableware</div>
    </div>
  </section>

  <section class="panel panel-side" aria-label="Box side with contents">
    <div class="side-list">
      <div class="side-item">
        <div class="plate plate-gold" role="img" aria-label="White dinner plate with gold rim"></div>
        <span class="side-label">25 Dinner Plates – 10.25"</span>
      </div>
      <div class="side-item">
        <div class="plate plate-rose" role="img" aria-label="White salad plate with rose gold rim"></div>
        <span class="side-label">25 Salad Plates – 7.5"</span>
      </div>
      <div class="side-item">
        <div class="forks" role="img" aria-label="Gold plastic forks, knife and spoon"></div>
        <span class="side-label">25 Forks – 7.4"</span>
      </div>
    </div>
  </section>

</body>
</html>
```